Cybersecurity company is looking for business card.

I need a business card design for our company, we are a cybersecurity company providing advance technology to protect agains any kind of malware. We need a fresh modern design it should communicate modern, technology and growth.

Target Market(s)

Business to business

Industry/Entity Type

Business

Contact Information for Business Card

Should have location, address, fax, mobile, phone, email and website.

Requirements
Must have
• Must follow company's logo color and style. Must have the company's log on its.

```html
<!DOCTYPE html>
<html lang="en">
<head>
<meta charset="utf-8">
<title>Vexora Business Card</title>
<link rel="stylesheet" href="https://fonts.googleapis.com/css2?family=Kotta+One&family=Arimo:wght@400;700&display=swap">
<style>
  :root {
    --backdrop: #b9b9b9;
    --card: #ebebeb;
    --crimson: #9d1b21;
    --ink: #151515;
    --paper-text: #f1e6e6;
  }
  * { margin: 0; padding: 0; box-sizing: border-box; }
  html, body { width: 1200px; height: 800px; overflow: hidden; }
  body {
    background: var(--backdrop);
    font-family: "Kotta One", Georgia, serif;
    color: var(--ink);
    position: relative;
  }
  .card {
    position: absolute;
    width: 540px;
    height: 310px;
    background: var(--card);
    border: 3px solid var(--crimson);
    overflow: hidden;
  }
  .card--front { left: 45px; top: 245px; }
  .card--back { left: 615px; top: 245px; }

  /* front */
  .front-band {
    position: absolute; left: 0; top: 182px;
    width: 300px; height: 42px; background: var(--crimson);
  }
  .front-logo-block {
    position: absolute; left: 40px; top: 112px;
    width: 250px; height: 112px; background: var(--crimson);
    display: flex; align-items: center; justify-content: center;
  }
  .brand-name {
    font-family: "Kotta One", Georgia, serif;
    color: var(--ink);
    letter-spacing: 1px;
    line-height: 1;
  }
  .front-logo-block .brand-name { font-size: 56px; }
  .location { font-size: 22px; white-space: nowrap; }
  .location .country { color: var(--crimson); }
  .front-location { position: absolute; left: 318px; top: 118px; }
  .front-contacts {
    position: absolute; left: 310px; top: 176px;
    display: flex; flex-direction: column; gap: 8px;
  }
  .contact-tag {
    display: flex; align-items: center; gap: 8px;
    background: var(--crimson); color: var(--paper-text);
    font-size: 13px; height: 24px; padding: 0 10px 0 4px;
    width: 212px;
  }
  .icon-chip {
    width: 18px; height: 18px; flex: none;
    display: flex; align-items: center; justify-content: center;
  }

  /* back */
  .back-header {
    position: absolute; left: 150px; top: 42px;
    display: flex; align-items: flex-end; gap: 18px;
  }
  .back-header .brand-name { font-size: 40px; }
  .back-header .location { font-size: 17px; padding-bottom: 4px; }
  .address-box {
    position: absolute; left: 18px; top: 100px;
    width: 262px; height: 92px; background: var(--crimson);
    color: var(--paper-text);
    display: flex; gap: 10px; padding: 12px 14px;
    font-size: 17px; line-height: 1.3;
  }
  .back-band {
    position: absolute; right: 0; top: 160px;
    width: 60px; height: 78px; background: var(--crimson);
  }
  .phone-box {
    position: absolute; right: 28px; top: 196px;
    width: 238px; height: 104px; background: var(--crimson);
    color: #fff; padding: 8px 14px;
    display: flex; flex-direction: column; justify-content: space-around;
    font-family: "Arimo", Arial, sans-serif; font-size: 16px;
  }
  .phone-line { display: flex; align-items: center; gap: 12px; }
  .phone-line .icon-chip { width: 20px; height: 20px; }
</style>
</head>
<body>

<section class="card card--front" aria-label="Business card front">
  <div class="front-band"></div>
  <div class="front-logo-block"><span class="brand-name">VEXORA</span></div>
  <p class="location front-location">Westport - <span class="country">Aldria</span></p>
  <ul class="front-contacts" style="list-style:none">
    <li class="contact-tag">
      <span class="icon-chip">
        <svg width="16" height="16" viewBox="0 0 16 16"><circle cx="8" cy="8" r="7" fill="none" stroke="#f1e6e6" stroke-width="1.2"/><rect x="4" y="5" width="8" height="6" fill="none" stroke="#f1e6e6" stroke-width="1"/><path d="M4 5l4 3 4-3" fill="none" stroke="#f1e6e6" stroke-width="1"/></svg>
      </span>
      name.surname@vexora.com
    </li>
    <li class="contact-tag">
      <span class="icon-chip">
        <svg width="16" height="16" viewBox="0 0 16 16"><rect x="1" y="1" width="14" height="14" rx="2" fill="none" stroke="#f1e6e6" stroke-width="1.2"/><circle cx="8" cy="8" r="4.5" fill="none" stroke="#f1e6e6" stroke-width="1"/><path d="M3.5 8h9M8 3.5v9" stroke="#f1e6e6" stroke-width="0.8"/></svg>
      </span>
      www.vexora.com
    </li>
  </ul>
</section>

<section class="card card--back" aria-label="Business card back">
  <div class="back-header">
    <span class="brand-name">VEXORA</span>
    <p class="location">Westport - <span class="country">Aldria</span></p>
  </div>
  <div class="address-box">
    <span class="icon-chip">
      <svg width="18" height="18" viewBox="0 0 18 18"><rect x="1" y="1" width="16" height="16" rx="3" fill="none" stroke="#f1e6e6" stroke-width="1.2"/><path d="M9 14s-4-4.2-4-7a4 4 0 0 1 8 0c0 2.8-4 7-4 7z" fill="none" stroke="#f1e6e6" stroke-width="1.2"/><circle cx="9" cy="7" r="1.4" fill="#f1e6e6"/></svg>
    </span>
    <p class="address-text">Harbor Tech Park (HTP) - Cedar Ring Road.</p>
  </div>
  <div class="back-band"></div>
  <div class="phone-box">
    <p class="phone-line">
      <span class="icon-chip">
        <svg width="20" height="20" viewBox="0 0 20 20"><rect x="1" y="1" width="18" height="18" rx="3" fill="none" stroke="#fff" stroke-width="1.2"/><rect x="5" y="8" width="10" height="7" fill="#fff"/><rect x="7" y="4" width="6" height="4" fill="none" stroke="#fff"/></svg>
      </span>
      04 555 0190
    </p>
    <p class="phone-line">
      <span class="icon-chip">
        <svg width="20" height="20" viewBox="0 0 20 20"><circle cx="10" cy="10" r="9" fill="none" stroke="#fff" stroke-width="1.2"/><path d="M7 5l2 3-1.2 1.2c.6 1.3 1.7 2.4 3 3L12 11l3 2-1 2c-4 0-8-4-8-8z" fill="none" stroke="#fff" stroke-width="1.1"/></svg>
      </span>
      04 555 0191
    </p>
    <p class="phone-line">
      <span class="icon-chip">
        <svg width="20" height="20" viewBox="0 0 20 20"><circle cx="10" cy="10" r="9" fill="none" stroke="#fff" stroke-width="1.2"/><rect x="7" y="4.5" width="6" height="11" rx="1" fill="none" stroke="#fff" stroke-width="1.1"/><circle cx="10" cy="13.5" r="0.8" fill="#fff"/></svg>
      </span>
      +971 50 555 019
    </p>
  </div>
</section>

</body>
</html>
```